Training flyer for 1/2 day modules

We need a flyer to be designed for some training sessions. It needs to be professional for the defence industry. It also needs to be able to be completed online - with tick boxes etc. Should be A4 back to back. Included in the documents below is some samples of previous brochures that we have had. Also below are some reviews from previous training - please use these somewhere;

- Great training, best I've ever had on this topic.
- Great presenter - very knowledgable.
- Course was very well presented and organised.

PLEASE USE MODULE TRAINING MOCK-UP FLYER ATTACHED FILE FOR CONTENT.

Target Market(s)

Defence industry

Industry/Entity Type

Defence

Requirements
Must have
• professional look - be able to be completed online,

```html
<!DOCTYPE html>
<html lang="en">
<head>
<meta charset="utf-8">
<title>Module Training Flyer</title>
<link href="https://fonts.googleapis.com/css2?family=Archivo+Black&family=Montserrat:wght@500;600&family=Open+Sans:wght@400;600;700&family=Roboto+Condensed:wght@300;400;700&display=swap" rel="stylesheet">
<style>
:root{
  --backdrop:#1e1e1e;
  --cream:#fdf6a8;
  --yellow:#fdf08a;
  --navy:#1b2f5e;
  --blue-light:#2a5b9c;
  --blue-dark:#0e2a55;
  --green:#3d8a1e;
  --ink:#1a1a1a;
  --white:#ffffff;
}
*{box-sizing:border-box;margin:0;padding:0}
html,body{width:1200px;height:1050px;overflow:hidden;background:var(--backdrop)}
.canvas{position:relative;width:1200px;height:1050px;background:var(--backdrop)}
.page{position:absolute;top:168px;width:504px;height:714px;overflow:hidden}
.page-front{left:78px;background:var(--cream)}
.page-back{left:618px;background:var(--white)}
.abs{position:absolute}

/* brand */
.brand{position:absolute;display:flex;align-items:center;gap:12px}
.brand-dot{width:76px;height:76px;border-radius:50%;background:var(--green)}
.brand-name{font-family:'Montserrat',sans-serif;font-weight:600;color:var(--green);font-size:23px;line-height:24px}
.contact{position:absolute;left:0;width:504px;text-align:center;font-family:'Montserrat',sans-serif;font-weight:500;font-size:10.5px;color:var(--ink)}

/* front */
.hero-bg{position:absolute;left:0;top:0}
.headline{position:absolute;font-family:'Archivo Black',sans-serif;color:var(--yellow);font-size:82px;line-height:1;white-space:nowrap;transform-origin:left top}
.eye-photo{position:absolute;left:143px;top:238px;width:84px;height:84px;border-radius:50%;background:linear-gradient(135deg,#d9d9d9,#9a9a9a)}
.sign-photo{position:absolute;left:258px;top:300px;width:128px;height:50px;background:linear-gradient(90deg,#8e2a3a,#24417e)}
.session-bar{position:absolute;left:62px;top:397px;width:380px;height:35px;background:#1c1c1c;color:var(--white);font-family:'Open Sans',sans-serif;font-weight:700;font-size:26px;letter-spacing:-1px;text-align:center;line-height:35px}
.city{position:absolute;top:441px;font-family:'Roboto Condensed',sans-serif;color:var(--yellow);line-height:1}
.city-name{font-weight:300;font-size:17px;letter-spacing:-0.4px}
.city-date{font-weight:700;font-size:17px;color:var(--yellow);letter-spacing:-0.5px}
.city-note{font-size:7px;font-weight:300;color:#d8dde8}
.city-rule{position:absolute;top:444px;width:1px;height:34px;background:var(--yellow)}
.review{position:absolute;left:0;width:504px;text-align:center;font-family:'Roboto Condensed',sans-serif;font-weight:300;font-size:18px;line-height:18px;letter-spacing:-0.9px;color:var(--white);text-transform:uppercase;white-space:nowrap}
.review-rule{position:absolute;left:65px;width:377px;height:1px;background:rgba(255,255,255,0.25)}
.module-one-title{position:absolute;left:11px;top:592px;width:210px;text-align:right;font-family:'Archivo Black',sans-serif;font-weight:400;font-size:19px;line-height:19px;color:var(--yellow);letter-spacing:-0.8px;text-transform:uppercase}
.module-one-body{position:absolute;left:270px;top:589px;width:182px;font-family:'Open Sans',sans-serif;font-size:8.4px;line-height:17.6px;color:var(--white)}

/* numbers */
.num{position:absolute;width:22px;height:22px;border-radius:50%;background:var(--ink);color:var(--white);font-family:'Open Sans',sans-serif;font-weight:700;font-size:12px;text-align:center;line-height:19px;border:1.5px solid var(--white)}
.vrule{position:absolute;width:1px}

/* back */
.module-title{position:absolute;left:61px;font-family:'Archivo Black',sans-serif;font-weight:400;font-size:21px;line-height:19px;color:var(--navy);letter-spacing:-0.7px;text-transform:uppercase}
.module-body{position:absolute;left:61px;width:190px;font-family:'Open Sans',sans-serif;font-size:7.8px;line-height:11.4px;color:var(--ink)}
.register{position:absolute;left:279px;top:46px;width:191px;height:424px;border:1px dashed #6a6a6a}
.register-title{position:absolute;left:11px;top:22px;font-family:'Archivo Black',sans-serif;font-weight:400;font-size:22px;line-height:20px;color:var(--navy);letter-spacing:-0.5px}
.field{position:absolute;left:11px;width:168px;display:flex;align-items:flex-end;font-family:'Open Sans',sans-serif;font-size:7.8px;color:var(--ink);line-height:10px;white-space:nowrap}
.field .line{flex:1;border-bottom:0.8px solid #333;margin-left:3px;height:8px}
.choices{position:absolute;left:11px;width:168px;display:flex;justify-content:space-between;font-family:'Open Sans',sans-serif;font-size:7.8px;color:var(--ink);line-height:10px}
.choice{display:flex;align-items:center;gap:3px}
.box{display:inline-block;width:20px;height:6px;border:0.8px solid #333;border-radius:2px}
.pay-label{position:absolute;left:11px;font-family:'Open Sans',sans-serif;font-weight:700;font-size:7.6px;color:var(--ink)}
.register-rule{position:absolute;left:11px;width:172px;height:1px;background:var(--navy);top:302px}
.price{position:absolute;left:161px;top:498px;width:178px;height:46px;border-radius:12px;background:var(--navy);color:var(--white);font-family:'Roboto Condensed',sans-serif;text-align:center;line-height:46px;font-size:20px;font-weight:300;letter-spacing:-0.5px}
.price strong{font-family:'Archivo Black',sans-serif;font-weight:400;font-size:19px}
.price small{font-size:10px}
</style>
</head>
<body>
<div class="canvas">

  <section class="page page-front">
    <svg class="hero-bg" width="504" height="714" viewBox="0 0 504 714">
      <defs>
        <radialGradient id="heroBlue" cx="50%" cy="45%" r="70%">
          <stop offset="0" stop-color="#2a5b9c"/>
          <stop offset="1" stop-color="#0e2a55"/>
        </radialGradient>
      </defs>
      <path d="M0 254 C110 190 230 176 330 190 C400 200 440 240 504 250 L504 714 L0 714 Z" fill="url(#heroBlue)"/>
      <path d="M0 254 C110 190 230 176 330 190 C400 200 440 240 504 250" fill="none" stroke="#1a1a1a" stroke-width="5"/>
    </svg>

    <div class="brand" style="left:140px;top:46px">
      <span class="brand-dot"></span>
      <span class="brand-name">Meridian<br>Trade<br>Compliance</span>
    </div>
    <p class="contact" style="top:144px">Level 2, 14-18 Harbour Lane, Kingsport &nbsp;|&nbsp; Phone: 61 (0)7 5550 0148</p>
    <p class="contact" style="top:160px">http://tradeready.example/info@meridiantc.example</p>

    <h1>
      <span class="headline" style="left:68px;top:258px">MODULE</span>
      <span class="headline" style="left:55px;top:320px;transform:scaleX(0.9);letter-spacing:-2px">TRAINING</span>
    </h1>
    <div class="eye-photo" role="img" aria-label="Close-up photo of an eye with a multicoloured iris"></div>
    <div class="sign-photo" role="img" aria-label="Photo of a wooden signpost painted with the Australian flag"></div>

    <div class="session-bar">Half day training sessions</div>

    <div class="city" style="left:93px"><div class="city-name">SYDNEY</div><div class="city-date">27 &amp; 28 April</div></div>
    <span class="city-rule" style="left:204px"></span>
    <div class="city" style="left:226px"><div class="city-name">CANBERRA</div><div class="city-date">29 April</div><div class="city-note">(modules 1 and 2 only)</div></div>
    <span class="city-rule" style="left:322px"></span>
    <div class="city" style="left:344px"><div class="city-name">BRISBANE</div><div class="city-date">2 &amp; 3 May</div></div>

    <p class="review" style="top:504px">Great training, best I've ever had on this topic.</p>
    <span class="review-rule" style="top:524px"></span>
    <p class="review" style="top:525px">Great presenter - very knowledgable.</p>
    <span class="review-rule" style="top:543px"></span>
    <p class="review" style="top:544px">Course was very well presented and organised.</p>

    <h2 class="module-one-title">Australian<br>Export<br>Controls<br>and AU/US<br>Trade Treaty</h2>
    <span class="vrule" style="left:245px;top:588px;height:104px;background:#ffffff"></span>
    <span class="num" style="left:234px;top:627px">1</span>
    <p class="module-one-body">This half day module provides attendees with guidance on Australian Export Controlsand the recent changes and provide guidance on management of the new requirements. Included in this session is information with regard to the Trade Co-operation Treaty.</p>
  </section>

  <section class="page page-back">
    <svg class="abs" style="left:0;top:0" width="504" height="714" viewBox="0 0 504 714">
      <path d="M0 0 L504 0 L504 466 C430 500 340 522 246 520 C150 518 60 490 0 460 Z" fill="#fdf6a8"/>
      <path d="M0 460 C60 490 150 518 246 520 C340 522 430 500 504 466" fill="none" stroke="#1b2f5e" stroke-width="3"/>
    </svg>

    <span class="vrule" style="left:40px;top:44px;height:110px;background:#555"></span>
    <span class="num" style="left:29px;top:88px">2</span>
    <h2 class="module-title" style="top:45px">Jurisdiction /<br>Classification?</h2>
    <p class="module-body" style="top:88px">This half day module will take attendees through export control reform and provide practical step by step guidance on Jurisdiction and Classification of U.S. controlled technology. Attendees will be encouraged to bring their own examples to be worked through during the training session.</p>

    <span class="vrule" style="left:40px;top:176px;height:140px;background:#555"></span>
    <span class="num" style="left:29px;top:233px">3</span>
    <h2 class="module-title" style="top:176px">Dual Nationals,<br>Discrimination<br>and Privacy</h2>
    <p class="module-body" style="top:238px">The contradiction between the U.S. Dual National Requirements &nbsp;Australian Anti-Discrimination has long been an issue for the Australian defence industry. Further compounding the issues is the new Australian Privacy Legislation. This module provides attendees with guidance on how to manage the issue and tip and hints on mitigation strategies.</p>

    <span class="vrule" style="left:40px;top:338px;height:126px;background:#555"></span>
    <span class="num" style="left:29px;top:391px">4</span>
    <h2 class="module-title" style="top:338px">Exemptions,<br>Exceptions &amp;<br>De Minimis</h2>
    <p class="module-body" style="top:401px">Exemptions, Exceptions and De-minimis primarily allows exporters to export U.S. controlled technology without prior approval, however, there are restrictions. This module will exploreExemptions, Exceptions and De-minimis and provide practical guidance on implementation and management.</p>

    <form class="register">
      <h2 class="register-title">HOW TO<br>REGISTER:</h2>

      <div class="field" style="top:68px">Attendee Name:<span class="line"></span></div>
      <div class="field" style="top:80px">Email:<span class="line"></span></div>
      <div class="choices" style="top:92px"><span class="choice">Sydney<span class="box"></span></span><span class="choice">Canberra<span class="box"></span></span><span class="choice">Brisbane<span class="box"></span></span></div>

      <div class="field" style="top:115px">Attendee Name:<span class="line"></span></div>
      <div class="field" style="top:127px">Email:<span class="line"></span></div>
      <div class="choices" style="top:139px"><span class="choice">Sydney<span class="box"></span></span><span class="choice">Canberra<span class="box"></span></span><span class="choice">Brisbane<span class="box"></span></span></div>

      <div class="field" style="top:161px">Attendee Name:<span class="line"></span></div>
      <div class="field" style="top:173px">Email:<span class="line"></span></div>
      <div class="choices" style="top:185px"><span class="choice">Sydney<span class="box"></span></span><span class="choice">Canberra<span class="box"></span></span><span class="choice">Brisbane<span class="box"></span></span></div>

      <div class="field" style="top:208px">Attendee Name:<span class="line"></span></div>
      <div class="field" style="top:220px">Email:<span class="line"></span></div>
      <div class="choices" style="top:232px"><span class="choice">Sydney<span class="box"></span></span><span class="choice">Canberra<span class="box"></span></span><span class="choice">Brisbane<span class="box"></span></span></div>

      <div class="field" style="top:255px">Company:<span class="line"></span></div>
      <div class="field" style="top:267px">Email:<span class="line"></span></div>
      <div class="field" style="top:279px">Phone:<span class="line"></span></div>

      <span class="register-rule"></span>

      <p class="pay-label" style="top:315px">PAYMENT METHOD:</p>
      <div class="choices" style="top:331px;width:124px"><span class="choice">Invoice<span class="box"></span></span><span class="choice">credit card<span class="box"></span></span></div>
      <div class="field" style="top:345px">Credit card number:<span class="line"></span></div>
      <div class="field" style="top:359px">Card name:<span class="line"></span></div>
      <div class="field" style="top:374px">Expiry date:<span class="line"></span></div>
      <div class="field" style="top:389px">CVV:<span class="line"></span></div>
      <div class="field" style="top:403px">Card holder email:<span class="line"></span></div>
    </form>

    <div class="price">PRICE: <strong>$495</strong> <small>(inc GST)</small></div>

    <div class="brand" style="left:148px;top:566px">
      <span class="brand-dot" style="width:72px;height:72px"></span>
      <span class="brand-name" style="font-size:21px;line-height:22px">Meridian<br>Trade<br>Compliance</span>
    </div>
    <p class="contact" style="top:665px">Level 2, 14-18 Harbour Lane, Kingsport &nbsp;|&nbsp; Phone: 61 (0)7 5550 0148</p>
    <p class="contact" style="top:682px">http://tradeready.example/info@meridiantc.example</p>
  </section>

</div>
</body>
</html>
```